Web Design Project

Looking to create a skin (just need PSD files) for our very simple publishing retail website (it only comprises of 2-3 pages but it has to be beautiful).

Also looking to create a logo in the style of the Grintax.com logo but slightly differant (ie has to be clear that they are related but not the same) The basic website has been built : http://quorvelstudio.example/inprogress/mm/WebDev/

The general look and feel which we are after is: the new tandrell, the new hivenook page, zelpo.fm (basically very web 2.0)

Full Brief Below:

The basic point of it is that as a student you can tell us which university you are at and then which course/degree you are studying and then up pops a list of all of the recommended text books which you can buy from corrind.

A very similar site is but we are much simpler than them: www.pupilbookrosters.example We want it to be very minimalist and clean, like zelpo.fm

The colour scheme (though not the design) should also match the following website www.grintax.example You can ignore the input boxes on the bottom right and top right of the web page as they are not meant to be there.

The entire website only has three pages,: 1. Home Page, 2. Results page with Modules.3. Results Page with Books (when clicked on it should take you to Corrind).

Target Market(s)

University Students

Industry/Entity Type

University

Requirements
Must have
• Specific Requirements:

1. Top of the page should be the new logo (similar to Grintax but differant, also needs a new name: e.g. Grintax Books or Grintax Reading, Grintax Physical, Grintax Old School, Grintax Books

2. Top of the page should be a paragraph of text and an image telling them what the website is.

3. Below that there should be two search boxes in a row, which list: University and Course. These should be auto fill (we have all the data, as per the attached spread sheet so they should only be able to select from these). When they select from these then they should be taken to another page listing all of the books, which pertain to this course & university (as per the website)

4. There should also be a general search bar in the top right hand corner this where they can just search normally for any book in our database. This will then produce a list of books wich you can then buy on corrind

5. There should also be another area of text which relates to how we get the data and saying that we will give students free books if they email us their reading lists (if we don’t have them) and then they can email us to get a free book once we have checked that the data is correct. This should be an autofill box. Which they put their email into.

6. There should also be a box saying that students should sign up to Grintax.com (this should be on every page)

```html
<!DOCTYPE html>
<html lang="en">
<head>
<meta charset="utf-8">
<title>Grintax Books</title>
<link rel="stylesheet" href="https://fonts.googleapis.com/css2?family=Arimo:wght@400;700&family=Open+Sans:wght@700&family=Roboto+Condensed:wght@300;400&display=swap">
<style>
:root{
  --brand:#2fa9e1;
  --brand-dark:#1d8fcb;
  --navy:#26458f;
  --navy-light:#3a5fae;
  --band:#e3e3e3;
  --page:#f2f2f2;
  --panel:#f9f9f9;
  --line:#cfcfcf;
  --text:#444;
  --muted:#555;
  --link:#1a8bc9;
  --heading:#2f9bd3;
  --white:#fff;
}
*{box-sizing:border-box;margin:0;padding:0}
html,body{width:1200px;height:1066px;overflow:hidden}
body{position:relative;background:var(--page);font-family:"Arimo",Arial,sans-serif;color:var(--text);font-size:12px}
.abs{position:absolute}

/* header */
.site-header{position:absolute;left:0;top:0;width:1200px;height:70px;background:var(--brand)}
.brand{left:141px;top:20px;color:var(--white);font-family:"Arimo",Arial,sans-serif;font-weight:700;font-size:26px;letter-spacing:-.5px}
.brand small{font-size:11px;font-weight:700;margin-left:4px;vertical-align:top;position:relative;top:4px}
.user-avatar{left:632px;top:15px;width:37px;height:37px;border-radius:4px;background:#f3f3f3}
.user-name{left:684px;top:26px;color:var(--white);font-family:"Open Sans",Arial,sans-serif;font-weight:700;font-size:13.5px}
.site-search{left:846px;top:22px;width:213px;height:28px;border-radius:14px;background:var(--white);border:2px solid #d9eef9;padding:6px 10px;font-size:11.5px;color:#555}
.site-search svg{position:absolute;right:9px;top:5px}

/* hero */
.hero-band{left:0;top:70px;width:1200px;height:385px;background:var(--band);border-bottom:1px solid #d4d4d4}
.hero-frame{left:142px;top:107px;width:917px;height:321px;border:1px solid var(--brand);padding:3px}
.hero-frame-inner{width:100%;height:100%;border:1px solid var(--brand)}
.hero-photo{left:150px;top:115px;width:901px;height:304px;background:linear-gradient(100deg,#d9cfa8 0%,#e6d98a 45%,#efe49a 70%,#d8c98a 100%)}
.hero-copy{left:539px;top:135px;font-family:"Roboto Condensed",Arial,sans-serif;color:#222}
.hero-copy h1{font-weight:400;font-size:26px;margin-bottom:10px}
.hero-copy li{list-style:none;font-weight:300;font-size:15px;display:flex;align-items:center;gap:9px;height:28px}
.hero-copy li:nth-child(3){margin-top:4px}
.bullet{width:12px;height:12px;border-radius:50%;background:#eee;border:1px solid #aaa;position:relative}
.bullet::after{content:"";position:absolute;left:4px;top:2.5px;border-left:4px solid #666;border-top:2.5px solid transparent;border-bottom:2.5px solid transparent}
.dots{left:582px;top:437px;display:flex;gap:6px}
.dots span{width:8px;height:8px;border-radius:50%;border:1px solid #888;background:var(--white)}
.dots span.on{background:var(--navy);border-color:var(--navy)}

/* course finder */
.finder{left:144px;top:493px;width:912px;height:65px;background:var(--panel);border:2px solid #ddd;border-radius:3px}
.label{font-size:12.5px;color:var(--muted)}
.field{height:24px;border-radius:12px;background:var(--white);border:1px solid #bbb;box-shadow:0 0 0 3px #e6e6e6}
.btn{background:var(--brand);color:var(--white);border-radius:3px;font-family:"Roboto Condensed",Arial,sans-serif;font-size:14px;text-align:center}

/* signup */
.signup{left:250px;top:585px;width:322px;height:82px;background:var(--white);border:1px solid #ddd;border-radius:4px}
.signup-btn{left:254px;top:588px;width:314px;height:73px;border-radius:3px;background:linear-gradient(#3b5fae,var(--navy));color:var(--white);font-family:"Roboto Condensed",Arial,sans-serif;font-size:31px;display:flex;align-items:center;justify-content:center;letter-spacing:.5px}

.section-title{font-family:"Roboto Condensed",Arial,sans-serif;font-weight:300;font-size:20px;color:var(--heading)}
.book{display:flex;align-items:center;gap:6px;font-size:12px;color:var(--muted)}
.tick{width:12px;height:12px;border:1px solid #777;background:var(--white);display:flex;align-items:center;justify-content:center}
.book a{color:var(--link)}

/* free books */
.free-books{left:668px;top:586px;width:388px;height:205px;background:var(--panel);border:2px solid #ddd;border-radius:3px}
.form-input{width:199px;height:22px;border:1px solid #bbb;border-radius:3px;background:var(--white)}

/* footer */
.site-footer{left:0;top:848px;width:1200px;height:218px;background:var(--white);border-top:1px solid #ddd}
.footer-col{top:864px}
.footer-col h3{font-family:"Roboto Condensed",Arial,sans-serif;font-weight:400;font-size:13.5px;color:var(--navy);margin-bottom:7px}
.footer-col li{list-style:none;font-size:11.5px;color:var(--muted);height:20.6px}
.social{width:30px;height:30px;border-radius:50%;top:891px}
</style>
</head>
<body>

<header class="site-header">
  <div class="abs brand">grintax<small>beta</small></div>
  <div class="abs user-avatar"></div>
  <div class="abs user-name">Marten Olsby</div>
  <div class="abs site-search">Search
    <svg width="16" height="16" viewBox="0 0 16 16"><circle cx="6" cy="6" r="4.5" fill="none" stroke="#333" stroke-width="1.6"/><line x1="9.5" y1="9.5" x2="14" y2="14" stroke="#333" stroke-width="2.2" stroke-linecap="round"/></svg>
  </div>
</header>

<section>
  <div class="abs hero-band"></div>
  <div class="abs hero-frame"><div class="hero-frame-inner"></div></div>
  <div class="abs hero-photo" role="img" aria-label="Photo of a young teacher reading a picture book to small children sitting on a classroom floor"></div>
  <div class="abs hero-copy">
    <h1>Study Smarter</h1>
    <ul>
      <li><span class="bullet"></span>The Best Free Education Content</li>
      <li><span class="bullet"></span>Share &amp; Collaborate As You Study</li>
      <li><span class="bullet"></span>Subscription Access To Course Textbooks</li>
    </ul>
  </div>
  <div class="abs dots"><span></span><span class="on"></span><span></span></div>
</section>

<form class="abs finder">
  <span class="abs label" style="left:12px;top:22px">University</span>
  <span class="abs field" style="left:78px;top:19px;width:183px"></span>
  <span class="abs label" style="left:328px;top:22px">Faculty</span>
  <span class="abs field" style="left:383px;top:19px;width:183px"></span>
  <span class="abs btn" style="left:593px;top:19px;width:48px;height:24px;line-height:24px">GO</span>
</form>

<div class="abs signup"></div>
<div class="abs signup-btn">STUDENTS SIGNUP</div>

<h2 class="abs section-title" style="left:142px;top:676px">Latest Books</h2>
<div class="abs" style="left:142px;top:714px;width:440px">
  <div class="abs book" style="left:0;top:0"><span class="tick"><svg width="9" height="9"><path d="M1 5l2.5 2.5L8 1" fill="none" stroke="#222" stroke-width="1.6"/></svg></span><a href="#" style="text-decoration:underline">Geomaterials Under The </a></div>
  <div class="abs book" style="left:0;top:28px"><span class="tick"><svg width="9" height="9"><path d="M1 5l2.5 2.5L8 1" fill="none" stroke="#222" stroke-width="1.6"/></svg></span>Pocket Handbook Of</div>
  <div class="abs book" style="left:0;top:56px"><span class="tick"><svg width="9" height="9"><path d="M1 5l2.5 2.5L8 1" fill="none" stroke="#222" stroke-width="1.6"/></svg></span>Carbonate Sediments &amp;</div>
  <div class="abs book" style="left:0;top:84px"><span class="tick"><svg width="9" height="9"><path d="M1 5l2.5 2.5L8 1" fill="none" stroke="#222" stroke-width="1.6"/></svg></span>Diseases Of Small Grain</div>
  <div class="abs book" style="left:224px;top:0"><span class="tick"><svg width="9" height="9"><path d="M1 5l2.5 2.5L8 1" fill="none" stroke="#222" stroke-width="1.6"/></svg></span>Avian Medicine</div>
  <div class="abs book" style="left:224px;top:28px"><span class="tick"><svg width="9" height="9"><path d="M1 5l2.5 2.5L8 1" fill="none" stroke="#222" stroke-width="1.6"/></svg></span>Oceanography</div>
  <div class="abs book" style="left:224px;top:56px"><span class="tick"><svg width="9" height="9"><path d="M1 5l2.5 2.5L8 1" fill="none" stroke="#222" stroke-width="1.6"/></svg></span>Ophthalmic Disease In</div>
  <div class="abs book" style="left:224px;top:84px"><span class="tick"><svg width="9" height="9"><path d="M1 5l2.5 2.5L8 1" fill="none" stroke="#222" stroke-width="1.6"/></svg></span>An Atlas Of Radiology Of</div>
</div>

<form class="abs free-books">
  <h2 class="abs section-title" style="left:13px;top:12px">Get your free books</h2>
  <span class="abs label" style="left:15px;top:63px;font-size:12px">Name</span>
  <span class="abs form-input" style="left:79px;top:58px"></span>
  <span class="abs label" style="left:15px;top:99px;font-size:12px">Email</span>
  <span class="abs form-input" style="left:79px;top:94px"></span>
  <span class="abs label" style="left:15px;top:136px;font-size:12px">University</span>
  <span class="abs form-input" style="left:79px;top:131px"></span>
  <span class="abs btn" style="left:79px;top:160px;width:60px;height:24px;line-height:24px">SUBMIT</span>
</form>

<footer class="abs site-footer"></footer>
<div class="abs footer-col" style="left:141px">
  <h3>Navigation</h3>
  <ul><li>Home</li><li>Resources</li><li>How it works</li><li>About us</li><li>News</li><li>Blog</li><li>Team</li></ul>
</div>
<div class="abs footer-col" style="left:325px;top:887px">
  <ul><li>Publishing Advisor Board</li><li>Educator Advisor Board</li><li>Job</li><li>Press</li><li>Publishing Partners</li><li>Technical Partners</li></ul>
</div>
<div class="abs footer-col" style="left:508px">
  <h3>Information</h3>
  <ul><li>Partners</li><li>Publishers</li><li>Academics</li><li>Codeharbor</li></ul>
</div>
<div class="abs footer-col" style="left:693px">
  <h3>Customer Services</h3>
  <ul><li>Contact us</li><li>FAQ</li><li>Privacy policy</li><li>Terms of Service</li><li>Content Takedown Request</li></ul>
</div>
<div class="abs footer-col" style="left:876px">
  <h3>Follow us on</h3>
</div>
<span class="abs social" style="left:876px;background:#3c5a98" aria-label="Social profile"></span>
<span class="abs social" style="left:912px;background:#2fa9e1" aria-label="Social profile"></span>
<span class="abs social" style="left:948px;background:#e4e4e4;border:1px solid #ccc" aria-label="Social profile"></span>

</body>
</html>
```